" Oferecemos consultoria e projetos nas áreas de saneamento e meio ambiente, atuamos home office. Temos o engenheiro sanitarista e ambiental e o gerente de marketing da empresa "

```html
<!DOCTYPE html>
<html lang="pt-BR">
<head>
<meta charset="UTF-8">
<title>Verdaria Ambiental – Cartão de visita</title>
<link href="https://fonts.googleapis.com/css2?family=Open+Sans:wght@400;600;700&display=swap" rel="stylesheet">
<style>
  :root{
    --bg:#e9e7e3;
    --card-dark:#3a3d40;
    --card-dark-edge:#2a2c2e;
    --brand-green:#5bb547;
    --leaf-green:#4aa63c;
    --teal:#5ec3c8;
    --teal-dark:#3fa8ae;
    --text-light:#d8dadb;
    --text-dark:#2f3133;
    --white:#ffffff;
    --band:#3b3e41;
  }
  *{margin:0;padding:0;box-sizing:border-box}
  html,body{width:1200px;height:1200px;overflow:hidden;background:var(--bg);font-family:"Open Sans",Arial,sans-serif}
  .canvas{position:relative;width:1200px;height:1200px}
  .card{position:absolute;left:150px;width:900px;height:500px;overflow:hidden;box-shadow:0 10px 30px rgba(0,0,0,.18)}

  /* Front */
  .card-front{top:70px;background:radial-gradient(ellipse at 50% 40%,var(--card-dark) 0%,var(--card-dark-edge) 100%)}
  .brand{position:absolute;top:150px;left:0;right:0;text-align:center}
  .brand-mark{display:inline-block;width:34px;height:34px;border-radius:50%;background:var(--brand-green);margin-bottom:14px}
  .brand-name{display:block;font-weight:700;font-size:74px;letter-spacing:-1px;color:var(--brand-green);line-height:1}
  .brand-tagline{display:block;margin-top:12px;font-size:19px;letter-spacing:6px;color:var(--text-light);font-weight:600}
  .front-band{position:absolute;left:0;right:0;bottom:0;height:58px;background:linear-gradient(90deg,var(--teal-dark),var(--teal));display:flex;align-items:center;justify-content:center;color:var(--white);font-size:15px;letter-spacing:1.6px;font-weight:600;text-transform:uppercase}

  /* Back */
  .card-back{top:630px;background:var(--white)}
  .contact{position:absolute;top:48px;right:70px;text-align:right;color:var(--text-dark)}
  .contact-name{font-size:22px;letter-spacing:1.5px;font-weight:600;text-transform:uppercase}
  .contact-role{font-size:17px;letter-spacing:4px;text-transform:uppercase;font-style:italic;color:#55595c;margin-top:4px}
  .contact-phone{font-size:22px;margin-top:46px}
  .contact-email{font-size:22px;margin-top:10px}
  .accent-bar{position:absolute;right:0;top:150px;width:14px;height:160px;background:var(--leaf-green)}
  .teal-line{position:absolute;left:0;right:0;bottom:150px;height:6px;background:var(--teal)}
  .services{position:absolute;left:0;right:0;bottom:0;height:150px;background:var(--band);display:grid;grid-template-columns:1fr 1fr;gap:0 40px;padding:28px 50px;color:var(--text-light);font-size:16px;line-height:1.7;list-style:none}
  .services li::before{content:"• "}
</style>
</head>
<body>
<main class="canvas">
  <section class="card card-front">
    <div class="brand">
      <span class="brand-mark"></span>
      <span class="brand-name">Verdaria Ambiental</span>
      <span class="brand-tagline">PROJETOS E CONSULTORIA</span>
    </div>
    <div class="front-band">Projetos e consultoria nas áreas de saneamento e meio ambiente</div>
  </section>

  <section class="card card-back">
    <div class="contact">
      <p class="contact-name">Marina Souza Ferreira</p>
      <p class="contact-role">Gerente Comercial</p>
      <p class="contact-phone">(48) 90000-1234</p>
      <p class="contact-email">contato@verdaria.com</p>
    </div>
    <div class="accent-bar"></div>
    <div class="teal-line"></div>
    <ul class="services">
      <li>Licenciamento Ambiental - LAPIS, LAI e LAO</li>
      <li>Captação e aproveitamento de água da chuva</li>
      <li>Gerenciamento de Resíduos Sólidos</li>
      <li>Projeto de saneamento: tratamento - água e esgoto</li>
      <li>Estudos Ambientais - RAP, ECA</li>
    </ul>
  </section>
</main>
</body>
</html>
```